IT COMPANYcutting edge tec business card

we are IT company that building any apps.
we need business card in japanese and english
You don’t have to include all information in front one you can attach part of that information to back-side
company name : 株式会社かすみ鳥 (MOSSLARK Inc.)
concept : cutting-edge technology
role : 取締役 (director)
name : 河 泰林 (Ha Taerimmu)
post number : 168-0037
address : 東京都世田谷区北霞台5-08-44 (5-08-44, Kitakasumidai, Setagaya Ku, Tokyo To, 168-0037, Japan)
Tel:+81-3-5917-2843
Mobile:+81-80-7263-5518
Email : taerimha@fieldoflark.com
website : www.fieldoflark.com

we dont have logo so please make it as well
we also looking for designer who can make homapage design.

Designs look the same

Low design quality

Contact Information for Business Card

cutting-edge design and modern for IT

Font styles to use
Sans Serif

Colors
34a6d7
33b8a4
6092c4
3377b5
886aae
6b449b
b868aa
a64599

Requirements
Must have
• Simple but designed

```html
<!DOCTYPE html>
<html lang="ja">
<head>
<meta charset="utf-8">
<title>MOSSLARK Inc. business card</title>
<link rel="stylesheet" href="https://fonts.googleapis.com/css2?family=Open+Sans:wght@400;600;700&family=Arimo:wght@400;700&family=Noto+Sans+JP:wght@400;700&display=swap">
<style>
  :root {
    --backdrop: #dcdde0;
    --card-grey: #4a4a4c;
    --card-white: #ffffff;
    --band-blue: #34a6d7;
    --brand-teal: #33b8a4;
    --ink: #1b1b1d;
    --ink-mute: #55565a;
    --ink-soft: #ffffff;
  }
  * { margin: 0; padding: 0; box-sizing: border-box; }
  html, body {
    width: 1200px; height: 780px; overflow: hidden;
    background: var(--backdrop);
  }
  .sheet {
    width: 1200px; height: 780px;
    display: flex; align-items: center; justify-content: center; gap: 40px;
  }
  .card {
    position: relative; width: 540px; height: 310px; overflow: hidden;
    box-shadow: 0 10px 28px rgba(0,0,0,.22);
  }
  .jp { font-family: "Noto Sans JP", "Arimo", sans-serif; }

  /* ---------- contact side ---------- */
  .card--contact { background: var(--card-white); }
  .contact-panel {
    position: absolute; right: 0; top: 0; width: 190px; height: 100%;
    background: var(--card-grey);
    display: flex; align-items: center; justify-content: center;
  }
  .address {
    position: absolute; left: 34px; top: 26px;
    font-family: "Arimo", Arial, sans-serif; font-size: 13px; line-height: 1.35;
    color: var(--ink); letter-spacing: .3px;
  }
  .contact-list {
    position: absolute; left: 34px; top: 96px; list-style: none;
    font-family: "Arimo", Arial, sans-serif; font-size: 13px; color: var(--ink);
    letter-spacing: .3px;
  }
  .contact-list li { display: flex; align-items: center; gap: 7px; height: 21px; }
  .contact-icon { width: 15px; height: 15px; flex: none; }
  .name-band {
    position: absolute; left: 0; top: 178px; width: 350px; height: 54px;
    background: var(--band-blue); padding: 7px 0 0 34px;
    font-family: "Arimo", Arial, sans-serif; color: var(--ink-soft);
  }
  .person-name { font-size: 17px; font-weight: 700; letter-spacing: .5px; line-height: 1.2; }
  .person-name .jp { font-size: 15px; margin-left: 10px; }
  .person-role { font-size: 13px; letter-spacing: .3px; line-height: 1.4; }
  .person-role .jp { font-size: 12px; margin-left: 8px; }
  .address-jp {
    position: absolute; left: 34px; top: 250px; width: 300px;
    font-size: 12px; line-height: 1.6; color: var(--ink-mute);
  }

  .brand {
    font-family: "Open Sans", Arial, sans-serif; font-weight: 600;
    color: var(--brand-teal); white-space: nowrap;
    display: flex; align-items: center;
  }
  .brand-dot { border-radius: 50%; background: var(--brand-teal); flex: none; }
  .brand-block { display: flex; flex-direction: column; align-items: center; gap: 6px; }
  .brand--small { font-size: 19px; gap: 6px; }
  .brand--small .brand-dot { width: 12px; height: 12px; }
  .brand-jp { font-size: 12px; color: var(--ink-soft); letter-spacing: 1px; }

  /* ---------- brand side ---------- */
  .card--brand { background: var(--card-grey); }
  .brand--large {
    position: absolute; left: 0; right: 0; top: 96px;
    justify-content: center; font-size: 38px; gap: 12px;
  }
  .brand--large .brand-dot { width: 24px; height: 24px; }
  .web-band { position: absolute; left: 0; bottom: 0; width: 540px; height: 104px; }
  .web-address {
    position: absolute; left: 0; right: 0; bottom: 48px; text-align: center;
    font-family: "Arimo", Arial, sans-serif; font-weight: 700; font-size: 16px;
    line-height: 20px; color: var(--ink); letter-spacing: .8px;
  }
</style>
</head>
<body>
<main class="sheet">

  <section class="card card--contact" aria-label="Contact side">
    <p class="address">5-08-44, Kitakasumidai<br>Setagaya Ku, Tokyo<br>To, 168-0037, Japan</p>
    <ul class="contact-list">
      <li>
        <svg class="contact-icon" viewBox="0 0 16 16" aria-hidden="true">
          <circle cx="8" cy="8" r="7.2" fill="none" stroke="var(--brand-teal)" stroke-width="1.4"/>
          <rect x="4.2" y="7.2" width="7.6" height="4" rx="1" fill="var(--brand-teal)"/>
          <path d="M3.8 6.6 Q8 3.6 12.2 6.6" fill="none" stroke="var(--brand-teal)" stroke-width="1.6"/>
        </svg>
        +81-3-5917-2843
      </li>
      <li>
        <svg class="contact-icon" viewBox="0 0 16 16" aria-hidden="true">
          <circle cx="8" cy="8" r="7.2" fill="none" stroke="var(--brand-teal)" stroke-width="1.4"/>
          <rect x="5.5" y="3.6" width="5" height="8.8" rx="1" fill="none" stroke="var(--brand-teal)" stroke-width="1.3"/>
          <circle cx="8" cy="10.6" r=".7" fill="var(--brand-teal)"/>
        </svg>
        +81-80-7263-5518
      </li>
      <li>
        <svg class="contact-icon" viewBox="0 0 16 16" aria-hidden="true">
          <circle cx="8" cy="8" r="7.6" fill="var(--brand-teal)"/>
          <rect x="4" y="5.2" width="8" height="5.6" fill="#fff"/>
          <path d="M4 5.2 L8 8.6 L12 5.2" fill="none" stroke="var(--brand-teal)" stroke-width="1"/>
        </svg>
        taerimha@fieldoflark.com
      </li>
    </ul>
    <div class="name-band">
      <p class="person-name">Ha Taerimmu<span class="jp">河 泰林</span></p>
      <p class="person-role">director<span class="jp">取締役</span></p>
    </div>
    <p class="address-jp jp">〒168-0037<br>東京都世田谷区北霞台5-08-44</p>
    <div class="contact-panel">
      <div class="brand-block">
        <p class="brand brand--small"><span class="brand-dot"></span>MOSSLARK Inc.</p>
        <p class="brand-jp jp">株式会社かすみ鳥</p>
      </div>
    </div>
  </section>

  <section class="card card--brand" aria-label="Brand side">
    <p class="brand brand--large"><span class="brand-dot"></span>MOSSLARK Inc.</p>
    <svg class="web-band" viewBox="0 0 540 104" aria-hidden="true">
      <path d="M0 62 H128 V36 Q128 20 146 20 H408 Q426 20 426 36 V62 H540 V104 H0 Z" fill="var(--band-blue)"/>
    </svg>
    <p class="web-address">www.fieldoflark.com</p>
  </section>

</main>
</body>
</html>
```